Beer Can Label design - HAZY NEIPA

Hazy NEIPA. (Acronym for New England India Pale Ale)
Full sleeve (473ml)
5.00" x 8.125" Inches
Write up on can reverse.
Opaque haze in appearance derived from specific oats, wheat, and water chemistry. This brew bolsters a dense and creamy head, leaving behind a soft and silky mouth-feel. Expect an intense tropical fruit centric aroma and flavour. Our timely hop additions contributes to less bitterness than typical IPA’s.
Logo is to be on front, towards bottom. Title near top.
Looking for something that stands out. Bold.
Target Market(s)
Craft beer enthusiasts
Industry/Entity Type
Beer & Brewing
Requirements
Must have
- Eye catching.

```html
<!DOCTYPE html>
<html lang="en">
<head>
<meta charset="utf-8">
<title>Hazy NEIPA – Can Label</title>
<link rel="stylesheet" href="https://fonts.googleapis.com/css2?family=Playfair+Display:wght@900&display=swap">
<style>
  :root {
    --page: #ffffff;
    --ink: #231f20;
    --night: #141313;
    --night-soft: #4a4545;
    --silver-dark: #9a9a9a;
    --silver-light: #e6e6e6;
    --orange-deep: #f26a12;
    --orange: #f7941d;
    --amber: #fbbf24;
    --yellow: #fcd82a;
    --cream: #ffffff;
  }
  html, body {
    margin: 0;
    width: 1200px;
    height: 1200px;
    overflow: hidden;
    background: var(--page);
  }
  .sheet {
    width: 1200px;
    height: 1200px;
    display: flex;
    flex-direction: column;
    align-items: center;
    justify-content: center;
    gap: 32px;
  }
  .label {
    display: block;
    width: 900px;
    height: 552px;
  }
  .label__title {
    font-family: "Playfair Display", Georgia, serif;
    font-weight: 900;
    text-anchor: middle;
  }
  .label__title--hazy { font-size: 96px; }
  .label__title--style { font-size: 92px; letter-spacing: -2px; }
  .label__brand {
    font-family: "Playfair Display", Georgia, serif;
    font-weight: 900;
    font-size: 46px;
    fill: var(--ink);
    text-anchor: middle;
  }
</style>
</head>
<body>
<main class="sheet">

  <svg class="label label--black" viewBox="0 0 1150 705" role="group" aria-label="Hazy NEIPA label, black edition">
    <defs>
      <linearGradient id="nightFill" x1="0" y1="0" x2="1" y2="0.3">
        <stop offset="0" stop-color="var(--night)"/>
        <stop offset="0.6" stop-color="#1f1d1d"/>
        <stop offset="1" stop-color="var(--night-soft)"/>
      </linearGradient>
      <linearGradient id="orangeFill" x1="0" y1="0" x2="1" y2="0">
        <stop offset="0" stop-color="var(--orange-deep)"/>
        <stop offset="0.35" stop-color="var(--orange)"/>
        <stop offset="0.7" stop-color="var(--amber)"/>
        <stop offset="1" stop-color="var(--yellow)"/>
      </linearGradient>
      <clipPath id="topClipA"><rect x="0" y="0" width="1150" height="430"/></clipPath>
      <clipPath id="bottomClipA"><rect x="0" y="430" width="1150" height="275"/></clipPath>
    </defs>

    <rect class="label__upper" x="0" y="0" width="1150" height="430" fill="url(#nightFill)"/>
    <g class="label__stripes" clip-path="url(#topClipA)" fill="#ffffff">
      <g transform="rotate(-42 575 215)">
        <rect x="-400" y="40" width="2000" height="60" rx="30" opacity="0.04"/>
        <rect x="-400" y="160" width="2000" height="110" rx="55" opacity="0.05"/>
        <rect x="-400" y="330" width="2000" height="40" rx="20" opacity="0.04"/>
        <rect x="-400" y="-160" width="2000" height="24" rx="12" opacity="0.18"/>
        <rect x="-400" y="-120" width="2000" height="8" rx="4" opacity="0.3"/>
      </g>
    </g>

    <rect class="label__lower" x="0" y="430" width="1150" height="275" fill="url(#orangeFill)"/>
    <g class="label__stripes" clip-path="url(#bottomClipA)">
      <g transform="rotate(-42 575 560)">
        <rect x="-400" y="420" width="2000" height="90" rx="45" fill="var(--yellow)" opacity="0.45"/>
        <rect x="-400" y="560" width="2000" height="60" rx="30" fill="var(--orange-deep)" opacity="0.25"/>
        <rect x="-400" y="680" width="2000" height="110" rx="55" fill="var(--yellow)" opacity="0.35"/>
        <rect x="-400" y="300" width="2000" height="50" rx="25" fill="var(--orange-deep)" opacity="0.2"/>
      </g>
    </g>

    <text class="label__title label__title--hazy" x="575" y="145" fill="var(--cream)">Hazy</text>
    <text class="label__title label__title--style" x="575" y="238" fill="var(--orange)">NEIPA</text>

    <g class="label__brand-mark">
      <circle cx="575" cy="470" r="16" fill="var(--ink)"/>
      <text class="label__brand" x="575" y="548">Foundry Row Brew House</text>
    </g>
  </svg>

  <svg class="label label--silver" viewBox="0 0 1150 705" role="group" aria-label="Hazy NEIPA label, silver edition">
    <defs>
      <linearGradient id="silverFill" x1="0" y1="0" x2="1" y2="0.3">
        <stop offset="0" stop-color="var(--silver-dark)"/>
        <stop offset="0.5" stop-color="#c4c4c4"/>
        <stop offset="1" stop-color="var(--silver-light)"/>
      </linearGradient>
      <linearGradient id="orangeFillB" x1="0" y1="0" x2="1" y2="0">
        <stop offset="0" stop-color="var(--orange-deep)"/>
        <stop offset="0.35" stop-color="var(--orange)"/>
        <stop offset="0.7" stop-color="var(--amber)"/>
        <stop offset="1" stop-color="var(--yellow)"/>
      </linearGradient>
      <clipPath id="topClipB"><rect x="0" y="0" width="1150" height="430"/></clipPath>
      <clipPath id="bottomClipB"><rect x="0" y="430" width="1150" height="275"/></clipPath>
    </defs>

    <rect class="label__upper" x="0" y="0" width="1150" height="430" fill="url(#silverFill)"/>
    <g class="label__stripes" clip-path="url(#topClipB)">
      <g transform="rotate(-42 575 215)">
        <rect x="-400" y="40" width="2000" height="60" rx="30" fill="#ffffff" opacity="0.18"/>
        <rect x="-400" y="160" width="2000" height="110" rx="55" fill="#ffffff" opacity="0.2"/>
        <rect x="-400" y="330" width="2000" height="40" rx="20" fill="#6f6f6f" opacity="0.15"/>
        <rect x="-400" y="-160" width="2000" height="24" rx="12" fill="#ffffff" opacity="0.4"/>
        <rect x="-400" y="-40" width="2000" height="70" rx="35" fill="#7a7a7a" opacity="0.15"/>
      </g>
    </g>

    <rect class="label__lower" x="0" y="430" width="1150" height="275" fill="url(#orangeFillB)"/>
    <g class="label__stripes" clip-path="url(#bottomClipB)">
      <g transform="rotate(-42 575 560)">
        <rect x="-400" y="420" width="2000" height="90" rx="45" fill="var(--yellow)" opacity="0.45"/>
        <rect x="-400" y="560" width="2000" height="60" rx="30" fill="var(--orange-deep)" opacity="0.25"/>
        <rect x="-400" y="680" width="2000" height="110" rx="55" fill="var(--yellow)" opacity="0.35"/>
        <rect x="-400" y="300" width="2000" height="50" rx="25" fill="var(--orange-deep)" opacity="0.2"/>
      </g>
    </g>

    <text class="label__title label__title--hazy" x="575" y="145" fill="var(--ink)">Hazy</text>
    <text class="label__title label__title--style" x="575" y="238" fill="var(--ink)">NEIPA</text>

    <g class="label__brand-mark">
      <circle cx="575" cy="470" r="16" fill="var(--ink)"/>
      <text class="label__brand" x="575" y="548">Foundry Row Brew House</text>
    </g>
  </svg>

</main>
</body>
</html>
```